New business card for my lawn and landscape business

Dorrin Yard and Building is a full-service lawn care, landscaping, and light construction company serving Paragould and the Northeast Arkansas region. The business is owned and operated by Marcus Toller, with a reputation for hands-on, detail-oriented service, dependable crews, and quality results for both residential and commercial clients. A well regarded business with great reviews.
Owner Marcus Toller
Dorrinyardandbuilding.example

Target Market(s)

Commercial, Middle, and upper class in north east Arkansas

Industry/Entity Type

Lawn maintenance and landscape

Contact Information for Business Card

Dorrin Yard And Building Professional lawn care, landscaping, and property improvement in Northeast Arkansas. • lawn maintenance •lawn treatments and weed control • exterior projects • Custom landscape design & installation • Sod, trees, rock & drainage solutions • Residential & commercial services Reliable. Detailed. Done right.

Requirements
Must have
• Business name, service area, list of some of our services, clean design that represents
Nice to have
• Unique. Different design element than just grass because its already in n the logo. Picture of a warm season (south) lawn or landscape. Pictures of the type of work we do

```html
<!DOCTYPE html>
<html lang="en">
<head>
<meta charset="utf-8">
<title>Dorrin Yard and Building — Business Card</title>
<link rel="stylesheet" href="https://fonts.googleapis.com/css2?family=Poppins:wght@400;500;600;700&display=swap">
<style>
  :root{
    --canvas:#e4e4e6;
    --leaf:#7cc242;
    --leaf-light:#a6d95c;
    --leaf-deep:#5fae2c;
    --white:#ffffff;
    --slate:#6d6e71;
    --ink:#4a4a4c;
    --rule:#c9c9cb;
  }
  *{box-sizing:border-box;margin:0;padding:0}
  html,body{width:1200px;height:900px;overflow:hidden;background:var(--canvas);font-family:"Poppins",sans-serif}
  .stage{position:relative;width:1200px;height:900px}
  .card{position:absolute;top:300px;width:520px;height:300px;border-radius:22px;overflow:hidden;box-shadow:0 10px 24px rgba(0,0,0,.12)}
  .card--front{left:50px}
  .card--back{left:630px;background:var(--white)}

  /* front */
  .front-bg{position:absolute;inset:0;background:radial-gradient(ellipse at 60% 10%,#8fcc4c 0%,transparent 55%),linear-gradient(135deg,var(--leaf) 0%,var(--leaf-light) 60%,#9bd054 100%)}
  .brand{position:absolute;display:flex;align-items:center;gap:9px}
  .brand__dot{width:20px;height:20px;border-radius:50%;flex:none}
  .brand__name{font-weight:600;letter-spacing:.4px;line-height:1.2;white-space:nowrap}
  .card--front .brand{left:30px;top:62px}
  .card--front .brand__dot{background:var(--white)}
  .card--front .brand__name{color:var(--white);font-size:17px}
  .front-copy{position:absolute;left:252px;top:46px;width:245px;color:var(--white)}
  .front-copy__lead{font-weight:700;font-size:12px;line-height:1.4;text-transform:uppercase;letter-spacing:.3px;margin-bottom:10px}
  .services{list-style:none;font-size:11.5px;line-height:1.55}
  .services li::before{content:"•";margin-right:6px}

  /* back */
  .back-top{position:absolute;left:0;top:0;width:100%;height:188px}
  .card--back .brand{left:28px;top:74px}
  .card--back .brand__dot{background:var(--leaf)}
  .card--back .brand__name{color:var(--leaf);font-size:15.5px}
  .divider{position:absolute;left:232px;top:34px;width:1px;height:138px;background:var(--rule)}
  .contact{position:absolute;left:258px;top:38px;color:var(--ink)}
  .contact__name{font-size:27px;font-weight:600;color:var(--leaf);line-height:1}
  .contact__role{font-size:12px;color:var(--slate);margin:4px 0 14px}
  .contact__list{list-style:none;font-size:12px;line-height:1.65}
  .contact__list li{display:flex;align-items:center;gap:8px}
  .contact__list svg{width:11px;height:11px;flex:none}
  .back-band{position:absolute;left:0;top:188px;width:100%;height:112px;background:var(--slate);color:var(--white);padding:22px 30px;font-size:12px;line-height:1.7}
  .back-band ul{list-style:none;display:flex;flex-wrap:wrap;column-gap:16px}
  .back-band li::before{content:"•";margin-right:6px}
</style>
</head>
<body>
<main class="stage">

  <section class="card card--front" aria-label="Card front">
    <div class="front-bg" role="img" aria-label="Soft-focus photo of a green lawn"></div>
    <div class="brand">
      <span class="brand__dot"></span>
      <span class="brand__name">DORRIN<br>YARD &amp; BUILDING</span>
    </div>
    <div class="front-copy">
      <p class="front-copy__lead">Dorrin Yard And Building professional lawn care, landscaping, and property improvement in Northeast Arkansas.</p>
      <ul class="services">
        <li>lawn maintenance</li>
        <li>lawn treatments and weed control</li>
        <li>Exterior Projects</li>
        <li>Sod, trees</li>
        <li>Custom landscape design &amp; installation</li>
        <li>rock &amp; drainage solutions</li>
      </ul>
    </div>
  </section>

  <section class="card card--back" aria-label="Card back">
    <div class="back-top">
      <div class="brand">
        <span class="brand__dot"></span>
        <span class="brand__name">DORRIN<br>YARD &amp; BUILDING</span>
      </div>
      <div class="divider"></div>
      <div class="contact">
        <h1 class="contact__name">JOHN SMITH</h1>
        <p class="contact__role">Designation</p>
        <ul class="contact__list">
          <li><svg viewBox="0 0 12 12"><path d="M2.5 1h2l1 3-1.5 1a6 6 0 0 0 3 3l1-1.5 3 1v2c0 .6-.4 1-1 1C5 11 1 7 1 2c0-.6.4-1 1.5-1z" fill="var(--leaf)"/></svg>(123) 444-5555</li>
          <li><svg viewBox="0 0 12 12"><circle cx="6" cy="6" r="5" fill="none" stroke="var(--leaf)" stroke-width="1.3"/><path d="M1 6h10M6 1c2 2.5 2 7.5 0 10M6 1c-2 2.5-2 7.5 0 10" fill="none" stroke="var(--leaf)" stroke-width="1"/></svg>www.YourWebsite.com</li>
          <li><svg viewBox="0 0 12 12"><rect x="1" y="2.5" width="10" height="7" rx="1" fill="var(--leaf)"/><path d="M1.5 3l4.5 3.5L10.5 3" fill="none" stroke="#fff" stroke-width="1"/></svg>your@email.com</li>
          <li><svg viewBox="0 0 12 12"><path d="M6 11S2 7 2 4.5a4 4 0 0 1 8 0C10 7 6 11 6 11z" fill="var(--leaf)"/><circle cx="6" cy="4.5" r="1.4" fill="#fff"/></svg>Your address, city 123</li>
        </ul>
      </div>
    </div>
    <div class="back-band">
      <ul>
        <li>lawn maintenance</li>
        <li>llawn treatments and weed control</li>
        <li>Sod, trees</li>
        <li>Exterior Projects</li>
        <li>Custom landscape design &amp; installation</li>
        <li>rock &amp; drainage solutions</li>
      </ul>
    </div>
  </section>

</main>
</body>
</html>
```